Facebook Ads for Leading Telemedicine Provider

Need a variation of this advertisement.

Would like to leave everything the same with white as the dominant color but test the pink circle with a different design style

Target Market(s)

Male / Female from 18-65

Industry/Entity Type

Health

Requirements
Must have
• Use the image attached and test a different background

```html
<!DOCTYPE html>
<html lang="en">
<head>
<meta charset="UTF-8">
<title>Free Covid Testing at Home — Medora</title>
<link rel="stylesheet" href="https://fonts.googleapis.com/css2?family=Hind:wght@500;600;700&display=swap">
<style>
  :root {
    --teal-deep: #0b4f56;
    --teal-mid: #17808a;
    --teal-light: #5fd0c0;
    --lens-glow: #bdf1e8;
    --white: #ffffff;
    --navy: #0e1c6b;
    --ink: #0a1633;
    --scene-warm: #e9c98a;
    --scene-cool: #3a9c94;
  }
  * { margin: 0; padding: 0; box-sizing: border-box; }
  html, body { width: 1200px; height: 1200px; overflow: hidden; }
  body { font-family: "Hind", Arial, sans-serif; }

  .ad {
    position: relative;
    width: 1200px;
    height: 1200px;
    overflow: hidden;
    background: radial-gradient(circle at 55% 45%, var(--teal-light) 0%, var(--teal-mid) 45%, var(--teal-deep) 100%);
  }

  .backdrop {
    position: absolute;
    inset: 0;
    background:
      radial-gradient(circle at 85% 12%, rgba(95, 208, 192, 0.55) 0 8%, transparent 18%),
      radial-gradient(circle at 90% 70%, rgba(20, 110, 110, 0.6) 0 10%, transparent 22%),
      radial-gradient(circle at 15% 92%, rgba(95, 208, 192, 0.35) 0 12%, transparent 25%);
  }

  .lens {
    position: absolute;
    left: 0;
    top: 194px;
    width: 752px;
    height: 752px;
    border-radius: 50%;
    background: radial-gradient(circle at 45% 40%, rgba(189, 241, 232, 0.55) 0%, rgba(23, 128, 138, 0.45) 70%, rgba(60, 70, 80, 0.55) 100%);
  }

  .brand {
    position: absolute;
    left: 141px;
    top: 78px;
    font-size: 72px;
    font-weight: 700;
    line-height: 1;
    color: var(--white);
  }

  .headline {
    position: absolute;
    left: 107px;
    top: 338px;
    font-size: 112px;
    font-weight: 600;
    line-height: 126px;
    color: var(--white);
    letter-spacing: -1px;
  }

  .cta {
    position: absolute;
    left: 173px;
    top: 771px;
    width: 425px;
    height: 96px;
    border-radius: 8px;
    background: var(--navy);
    color: var(--white);
    font-size: 42px;
    font-weight: 600;
    display: flex;
    align-items: center;
    justify-content: center;
    letter-spacing: 0.5px;
  }

  .home-visit {
    position: absolute;
    left: 604px;
    top: 513px;
    width: 548px;
    height: 559px;
    border-radius: 24px;
    background: linear-gradient(160deg, var(--scene-warm) 0%, var(--scene-cool) 100%);
    opacity: 0.85;
  }

  .web-address {
    position: absolute;
    left: 176px;
    top: 1128px;
    font-size: 32px;
    font-weight: 500;
    color: var(--ink);
  }
</style>
</head>
<body>
  <main class="ad">
    <div class="backdrop" role="img" aria-label="Teal background scattered with virus particles"></div>
    <div class="lens" role="img" aria-label="Magnifying glass enlarging a virus particle"></div>

    <div class="brand">Medora</div>

    <h1 class="headline">Free Covid<br>Testing at<br>Home</h1>

    <div class="cta">BOOK NOW</div>

    <div class="home-visit" role="img" aria-label="A woman opens her front door to a masked health worker with a clipboard, beside a crossed-out virus sign and a check badge"></div>

    <p class="web-address">https://medora.org/covid-testing</p>
  </main>
</body>
</html>
```